Design a Logo and business card for my real estate company

Harborline Estates- this is the company

Miles Tranbury
Broker - Realtor - Investor
925-555-0173
BRE# 07391826

```html
<!DOCTYPE html>
<html lang="en">
<head>
<meta charset="UTF-8">
<title>Miles Tranbury – Business Card</title>
<link href="https://fonts.googleapis.com/css2?family=Michroma&family=Arimo:wght@400;700&display=swap" rel="stylesheet">
<style>
  :root {
    --red-deep: #b5121b;
    --red-mid: #d8151d;
    --red-bright: #f3191f;
    --ink-light: #ffffff;
  }
  html, body {
    margin: 0;
    padding: 0;
    width: 1200px;
    height: 685px;
    overflow: hidden;
    background: #ffffff;
  }
  .card {
    position: relative;
    width: 1200px;
    height: 685px;
    overflow: hidden;
    color: var(--ink-light);
    background:
      radial-gradient(ellipse at 85% 40%, rgba(255, 40, 40, 0.35), transparent 60%),
      linear-gradient(100deg, var(--red-deep) 0%, var(--red-mid) 45%, var(--red-bright) 100%);
  }
  .brand {
    position: absolute;
    left: 60px;
    top: 300px;
    width: 500px;
    display: flex;
    align-items: center;
    justify-content: center;
    gap: 18px;
  }
  .brand-mark {
    width: 30px;
    height: 30px;
    background: var(--ink-light);
    flex: none;
  }
  .brand-name {
    font-family: "Michroma", sans-serif;
    font-size: 31px;
    font-weight: 400;
    white-space: nowrap;
  }
  .divider {
    position: absolute;
    left: 596px;
    top: 110px;
    width: 7px;
    height: 472px;
    background: var(--ink-light);
  }
  .contact {
    position: absolute;
    left: 640px;
    top: 228px;
  }
  .contact-name {
    margin: 0 0 30px;
    font-family: "Michroma", sans-serif;
    font-size: 34px;
    font-weight: 400;
    letter-spacing: 1px;
  }
  .contact-line {
    margin: 0 0 26px;
    font-family: "Arimo", sans-serif;
    font-size: 29px;
    line-height: 31px;
    letter-spacing: 0.5px;
  }
  .contact-line sup {
    font-size: 17px;
    vertical-align: 8px;
  }
  .website {
    position: absolute;
    left: 0;
    right: 0;
    top: 608px;
    text-align: center;
    font-family: "Arimo", sans-serif;
    font-weight: 700;
    font-size: 21px;
    letter-spacing: 18px;
    padding-left: 18px;
  }
</style>
</head>
<body>
  <main class="card">
    <div class="brand">
      <span class="brand-mark"></span>
      <span class="brand-name">Miles Tranbury</span>
    </div>

    <div class="divider"></div>

    <section class="contact">
      <h1 class="contact-name">Miles Tranbury</h1>
      <p class="contact-line">Broker - Realtor - Investor</p>
      <p class="contact-line">925-555-0173</p>
      <p class="contact-line">BRE<sup>#</sup> 07391826</p>
    </section>

    <p class="website">www.harborlinehomes.com</p>
  </main>
</body>
</html>
```